Business Card Design Project for a Restaurant/Wine Bar

New, fresh business card design for Verdano Wine Bar & Restaurant, Calder Cove, Westmark. We are an established restaurant on the Westmark coast featuring "Italian coastal cuisine."

"Verdano" means bay leaf in Italian. We aren't sure if we would like our logo on the card or not, but if you have something interesting that uses it, then please do so. The basic information is essential - full restaurant name, address, phone and website (do not use www). The font on our menu and wine list may give you some sort of an idea of our style.

One-sided card needed as we often use the backside to write down various types of info for customers.

After seeing a few submissions, we would like to see what designers can come up with-using the logo, just the leaf, or none at all. Sky is the limit as long as our full restaurant name, address, phone and website (please leave out www) are there. Please contact us if questions!

I appreciate all of your designs! Our deadline is next week, but I will continue to give feedback on designs as I can. This is our busiest season, so my co-owner/chef/husband, won't have time to look at the designs for awhile. When he does, we can make our decision.

cheers,
Mirel

Target Market(s)

Fine dining/wine crowd. Would like something simple and elegant, but not pretentious or stuffy. Verdano means bay laurel (bay leaf) in Italian (please see our logo).

Industry/Entity Type

Restaurant

Requirements
Must have
• Full Name of Restaurant: Verdano Wine Bar & Restaurant
Address: 812 Fenwick Ave NW, Calder Cove, Westmark 97538
Phone: 555.555.0193
website: verdanowinebar.example (do not use www)
Should not have
• Loud colors.

```html
<!DOCTYPE html>
<html lang="en">
<head>
<meta charset="utf-8">
<title>Verdano Wine Bar &amp; Restaurant — Business Card</title>
<link rel="stylesheet" href="https://fonts.googleapis.com/css2?family=Arimo:wght@400;700&family=Nothing+You+Could+Do&display=swap">
<style>
  :root {
    --backdrop: #e9e4dc;
    --sage: #97ad90;
    --sage-deep: #8aa283;
    --bark: #574b3f;
    --cream: #f8e7c0;
    --ink: #4a3f34;
  }
  * { margin: 0; padding: 0; box-sizing: border-box; }
  html, body {
    width: 1200px;
    height: 900px;
    overflow: hidden;
    background: var(--backdrop);
  }
  .canvas {
    position: relative;
    width: 1200px;
    height: 900px;
  }
  .card {
    position: absolute;
    left: 100px;
    top: 164px;
    width: 1000px;
    height: 572px;
    background: var(--sage);
    overflow: hidden;
    box-shadow: 0 6px 18px rgba(60, 50, 40, 0.18);
  }
  .leaf-texture {
    position: absolute;
    inset: 0;
    background: radial-gradient(ellipse at 30% 40%, var(--sage-deep), var(--sage) 70%);
  }
  .card-band {
    position: absolute;
    left: 0;
    right: 0;
    top: 246px;
    height: 80px;
    background: var(--bark);
  }
  .label-frame {
    position: absolute;
    inset: 0;
  }
  .label-content {
    position: absolute;
    left: 190px;
    width: 620px;
    top: 140px;
    text-align: center;
    color: var(--ink);
  }
  .brand-name {
    font-family: "Arimo", Arial, sans-serif;
    font-weight: 700;
    font-size: 72px;
    letter-spacing: 7px;
    line-height: 1;
    color: var(--bark);
  }
  .full-name {
    margin-top: 36px;
    font-family: "Nothing You Could Do", cursive;
    font-size: 36px;
    line-height: 1.15;
    color: var(--ink);
  }
  .contact {
    margin-top: 18px;
    font-family: "Arimo", Arial, sans-serif;
    font-size: 23px;
    line-height: 1.4;
    color: var(--ink);
    font-style: normal;
  }
</style>
</head>
<body>
<main class="canvas">
  <section class="card" aria-label="Verdano Wine Bar &amp; Restaurant business card">
    <div class="leaf-texture" role="img" aria-label="Faint bay leaf pattern across the sage green background"></div>
    <div class="card-band"></div>
    <svg class="label-frame" width="1000" height="572" viewBox="0 0 1000 572" aria-hidden="true">
      <path d="M240,66 L760,66 Q816,66 822,118 Q852,286 822,454 Q816,506 760,506 L240,506 Q184,506 178,454 Q148,286 178,118 Q184,66 240,66 Z"
            fill="var(--cream)" stroke="var(--bark)" stroke-width="16"/>
      <path d="M246,86 L754,86 Q800,86 805,128 Q832,286 805,444 Q800,486 754,486 L246,486 Q200,486 195,444 Q168,286 195,128 Q200,86 246,86 Z"
            fill="none" stroke="var(--bark)" stroke-width="3"/>
    </svg>
    <div class="label-content">
      <h1 class="brand-name">VERDANO</h1>
      <p class="full-name">Verdano Wine Bar &amp; Restaurant</p>
      <address class="contact">
        812 Fenwick Ave NW, Calder Cove, Westmark 97538<br>
        555.555.0193<br>
        verdanowinebar.example
      </address>
    </div>
  </section>
</main>
</body>
</html>
```